Wine Label Design

Organization name: Orvell Wine Company

My company is called Orvell Wine Company, I’m a wine importer and wholesaler who distributes wine domestically.

We are about to launch a line of three premium and one sparkling wine that we will wholesale to various retailers, wine stores, and restaurants for re-sale. The wines label will have “Dean Marlowe” I plan on having the labels the same and just changing the varietal as needed. My wine are made from premium grapes and will be marketed as a high end wine. My current label size is 3 1/2" wide by 5" in long and the labels can be on a solid background or transparent.

I would like the first label to be for my Cabernet Sauvignon, California, 2012, 750ML (for the size of the bottle) and ALC 13.8% BY VOL (for the alcohol content).

Colors: I am open to any and all designs that would alter my perception of what will be best!

Further:
Current label is boring and poorly done, so hopefully you designers can come up with something better

Industry/Entity Type

It Company

```html
<!DOCTYPE html>
<html lang="en">
<head>
<meta charset="utf-8">
<title>Dean Marlowe Cabernet Sauvignon Label</title>
<link rel="stylesheet" href="https://fonts.googleapis.com/css2?family=Cabin:wght@400;500;600;700&display=swap">
<style>
  :root {
    --backdrop: #d4d1d1;
    --label-white: #fbfbfa;
    --gold: #f2c01c;
    --wine-red: #b3121e;
    --ink-grey: #6a6a6a;
  }
  * { margin: 0; padding: 0; box-sizing: border-box; }
  html, body {
    width: 848px;
    height: 1200px;
    overflow: hidden;
    background: var(--backdrop);
  }
  .canvas {
    position: relative;
    width: 848px;
    height: 1200px;
    background: var(--backdrop);
    font-family: "Cabin", sans-serif;
  }
  .label {
    position: absolute;
    left: 164px;
    top: 60px;
    width: 520px;
    height: 1080px;
    background: var(--label-white);
    text-align: center;
  }
  .brand-mark {
    position: absolute;
    left: 50%;
    top: 150px;
    width: 150px;
    height: 150px;
    margin-left: -75px;
    border-radius: 50%;
    background: var(--gold);
  }
  .brand-name {
    position: absolute;
    left: 0;
    right: 0;
    top: 500px;
    color: var(--gold);
    font-weight: 600;
    font-size: 64px;
    line-height: 60px;
    letter-spacing: 3px;
    text-transform: uppercase;
  }
  .varietal {
    position: absolute;
    left: 0;
    right: 0;
    top: 716px;
    color: var(--wine-red);
    font-weight: 600;
    font-size: 35px;
    letter-spacing: 0.5px;
  }
  .region {
    position: absolute;
    left: 0;
    right: 0;
    top: 786px;
    color: var(--ink-grey);
    font-size: 22px;
    letter-spacing: 2px;
  }
  .vintage {
    position: absolute;
    left: 0;
    right: 0;
    top: 908px;
    color: var(--wine-red);
    font-weight: 600;
    font-size: 35px;
  }
  .details {
    position: absolute;
    left: 62px;
    right: 62px;
    top: 980px;
    display: flex;
    justify-content: space-between;
    color: var(--ink-grey);
    font-size: 22px;
  }
  .details sup {
    font-size: 12px;
    letter-spacing: 0.5px;
  }
</style>
</head>
<body>
  <main class="canvas">
    <section class="label">
      <div class="brand-mark"></div>
      <h1 class="brand-name">Dean<br>Marlowe</h1>
      <p class="varietal">CABERNET SAUVIGNON</p>
      <p class="region">CALIFORNIA</p>
      <p class="vintage">2012</p>
      <div class="details">
        <span class="volume">750<sup>ML</sup></span>
        <span class="alcohol">13.8%<sup>ALC</sup></span>
      </div>
    </section>
  </main>
</body>
</html>
```